Counseling Practice Business Card

I need a professional looking business card incorporating my new logo that was just completed. Card needs to incorporate my name and title, description of my specialty, my address, my phone number, my fax number, my email and my website URL. I need to be able to choose design on/with different paper colors and textures.
I do not have a lot of business card ideas so I am open to anything but I want bold,sharp, clear card without additional designs other than my logo (see attached file info). I am open to different color backgrounds or paper colors including black. I do not like traditional brackets around area codes in phone number or dashes between numbers in phone number. Am open to other ways of presenting including periods between numbers as appropriate. I do not know enough to know what I like yet but I want card to coordinate and work together with my logo. My practice emphasizes natural mental health interventions so any use of color (with background paper color or the blue and green in my logo) that elicits nature is nice. In addition to black, any natural brown or wood looking background might be desirable also. Most of the offerings so far look very similar and boring.

Target Market(s)

Potential therapy clients and other professionals

Contact Information for Business Card

Card information:
Marcus T. Whitfield, Ph.D.
Licensed Clinical Psychologist
Integrative Health Coach
4812 Ferndale Pkwy NW
Suite 730
Duluth, GA 30096
(770) 555-0142 phone
(770) 555-0186 fax
drmarcuswhitfield@kelvora.com
pathbloomcounseling.com

Font styles to use
Serif
Sans Serif
Other font styles liked:
• anything that you think looks crisp, clear and easily readable

Requirements
Must have
• Any color used should coordinate with my logo design (see attached files).
• Card should be printed horizontally so top and bottom are longest sides of rectangle.
• Background color or paper color should complement and highlight logo. Do not like a white background. black, grey, brown or any color my logo would blend well with.
Nice to have
• I would like designer to utilize color to highlight letters/name or phone-fax-web symbols.
• Bottom edge of card could be highlighted if appropriate to an idea.
Should not have
• I would NOT want the card to have a pure white background at all.
• No clear cards.
• Cards should be oriented with long sides on bottom and top, NOT sides. DO NOT LIKE THIS THIN TALL ORIENTATION.

```html
<!DOCTYPE html>
<html lang="en">
<head>
<meta charset="utf-8">
<title>Pathbloom Counseling – Business Card</title>
<link href="https://fonts.googleapis.com/css2?family=Tinos:wght@400;700&display=swap" rel="stylesheet">
<style>
  :root {
    --page: #ffffff;
    --card-brown: #653322;
    --tan: #d3a587;
    --tan-text: #d8ab8c;
    --name-brown: #6a3424;
  }
  html, body {
    margin: 0;
    padding: 0;
    width: 1200px;
    height: 1200px;
    overflow: hidden;
    background: var(--page);
  }
  .canvas {
    position: relative;
    width: 1200px;
    height: 1200px;
    font-family: "Tinos", "Times New Roman", serif;
  }
  .card {
    position: absolute;
    left: 179px;
    top: 298px;
    width: 871px;
    height: 510px;
    background: var(--card-brown);
    overflow: hidden;
  }
  .name-tab {
    position: absolute;
    left: 450px;
    top: 0;
    width: 421px;
    height: 143px;
    background: var(--tan);
    border-bottom-left-radius: 34px;
  }
  .name {
    position: absolute;
    left: 17px;
    top: 44px;
    margin: 0;
    font-size: 28px;
    font-weight: 700;
    letter-spacing: 0.3px;
    color: var(--name-brown);
    white-space: nowrap;
  }
  .titles {
    position: absolute;
    left: 56px;
    top: 78px;
    margin: 0;
    padding: 0;
    list-style: none;
    color: var(--name-brown);
    font-size: 21px;
    line-height: 28px;
  }
  .titles li {
    position: relative;
    padding-left: 25px;
    white-space: nowrap;
  }
  .titles li::before {
    content: "";
    position: absolute;
    left: 0;
    top: 10px;
    width: 10px;
    height: 10px;
    background: var(--name-brown);
  }
  .brand {
    position: absolute;
    left: 40px;
    top: 232px;
    width: 390px;
    margin: 0;
    color: var(--tan-text);
    font-size: 34px;
    font-weight: 400;
    line-height: 44px;
    text-align: center;
    white-space: nowrap;
  }
  .address {
    position: absolute;
    left: 452px;
    top: 166px;
    margin: 0;
    font-style: normal;
    color: var(--tan-text);
    font-size: 23px;
    line-height: 38px;
  }
  .contact {
    position: absolute;
    left: 450px;
    top: 292px;
    margin: 0;
    padding: 0;
    list-style: none;
    color: var(--tan-text);
    font-size: 23px;
  }
  .contact li {
    display: flex;
    align-items: center;
    height: 30px;
    white-space: nowrap;
  }
  .contact li + li { margin-top: 16px; }
  .contact li.phone + li.fax { margin-top: 18px; }
  .contact li.email { margin-top: 12px; }
  .contact .icon {
    width: 28px;
    height: 28px;
    margin-right: 9px;
    flex: none;
    fill: var(--tan-text);
  }
  .dot {
    display: inline-block;
    width: 7px;
    height: 7px;
    background: var(--tan-text);
    margin: 0 5px;
    vertical-align: middle;
    position: relative;
    top: -2px;
  }
</style>
</head>
<body>
<div class="canvas">
  <section class="card">
    <div class="name-tab">
      <h1 class="name">Marcus T. Whitfield, Ph.D.</h1>
      <ul class="titles">
        <li>Licensed Clinical Psychologist</li>
        <li>Integrative Health Coach</li>
      </ul>
    </div>

    <p class="brand">Pathbloom Counseling</p>

    <address class="address">
      4812 Ferndale Pkwy NW<br>
      Suite 730<br>
      Duluth, GA 30096
    </address>

    <ul class="contact">
      <li class="phone">
        <svg class="icon" viewBox="0 0 28 28" aria-hidden="true">
          <path d="M6 2 L10 2 L12 8 L9 10 Q11 17 15 22 L18 20 L22 24 L19 27 Q12 25 8 17 Q4 9 6 2 Z"/>
        </svg>
        <span>770<span class="dot"></span>555<span class="dot"></span>0142</span>
      </li>
      <li class="fax">
        <svg class="icon" viewBox="0 0 28 28" aria-hidden="true">
          <path d="M7 2 H21 V8 H7 Z M3 9 H25 Q27 9 27 11 V20 H23 V16 H5 V20 H1 V11 Q1 9 3 9 Z M6 18 H22 V27 H6 Z"/>
        </svg>
        <span>770<span class="dot"></span>555<span class="dot"></span>0186</span>
      </li>
      <li class="email">
        <svg class="icon" viewBox="0 0 28 28" aria-hidden="true">
          <path d="M1 5 H27 V23 H1 Z M4 8 V20 H24 V8 L14 16 Z M5 7 L14 14 L23 7 Z" fill-rule="evenodd"/>
        </svg>
        <span>drmarcuswhitfield@kelvora.com</span>
      </li>
      <li class="web">
        <svg class="icon" viewBox="0 0 28 28" aria-hidden="true">
          <g fill="none" stroke="#d8ab8c" stroke-width="2">
            <circle cx="14" cy="14" r="12"/>
            <ellipse cx="14" cy="14" rx="5" ry="12"/>
            <line x1="2" y1="14" x2="26" y2="14"/>
            <line x1="4" y1="8" x2="24" y2="8"/>
            <line x1="4" y1="20" x2="24" y2="20"/>
          </g>
        </svg>
        <span>www.pathbloomcounseling.com</span>
      </li>
    </ul>
  </section>
</div>
</body>
</html>
```